I want a website for a digital media and music production company named brambleton media

I want a website e commerce, that showcases our experience and projects, and sells merchandise and others.
we will use ai, produce webcasts, podcasts, musical talent.
we have the recording studios staff and equipment to produce and manage talent. We are an influencer factory and top content producers for social media radio and tv.
Must be able to stream video, podcasts, monetize, and have pay to view options.
we need a content manage system to change , upload video and images content constantly-

```html
<!DOCTYPE html>
<html lang="en">
<head>
<meta charset="utf-8">
<title>Brambleton Media</title>
<link href="https://fonts.googleapis.com/css2?family=Outfit:wght@400;500;600&display=swap" rel="stylesheet">
<style>
:root{
  --bg:#141313;
  --bg-deep:#0f0f0f;
  --accent:#b88b5e;
  --accent-dark:#2a1c10;
  --text:#ffffff;
  --muted:#d9d4cf;
  --frame:#3a3530;
}
*{margin:0;padding:0;box-sizing:border-box}
html,body{width:1200px;height:3556px;overflow:hidden}
body{background:var(--bg);color:var(--text);font-family:"Outfit",sans-serif;position:relative}
.abs{position:absolute}
.hero{left:0;top:0;width:1200px;height:470px;background:linear-gradient(180deg,#1e2428 0%,#2a2a2c 35%,#3a2e24 55%,#1a1816 85%,var(--bg) 100%)}
.city-band{left:0;top:150px;width:1200px;height:220px;background:radial-gradient(ellipse at 50% 40%,rgba(120,90,60,.35),rgba(0,0,0,0) 70%)}
.icon-btn{width:44px;height:44px;background:var(--accent);display:flex;align-items:center;justify-content:center}
.brand{left:0;width:1200px;text-align:center;color:var(--accent);font-weight:500;letter-spacing:10px;line-height:1.15}
.brand.top{top:200px;font-size:38px}
.tagline{left:0;top:318px;width:1200px;text-align:center;font-size:14px;letter-spacing:.2px}
.btn{background:var(--accent);color:var(--accent-dark);font-weight:600;font-size:14px;display:flex;align-items:center;justify-content:center;letter-spacing:.2px}
h2{font-weight:600;font-size:44px;line-height:1;letter-spacing:-.3px}
h2 span{color:var(--accent)}
.copy{font-size:14.5px;line-height:30px;width:450px}
.photo{border-radius:4px}
.play{width:30px;height:30px;border-radius:50%;background:var(--accent);display:flex;align-items:center;justify-content:center}
.center{left:0;width:1200px;text-align:center}
.merch-card-frame{left:445px;top:1513px;width:309px;height:320px;border:2px solid var(--frame)}
.merch-label{font-size:17px;font-weight:500;width:250px;text-align:center}
.arrow{width:42px;height:42px;border-radius:50%;background:#2b2927;border:1px solid #3c3936;display:flex;align-items:center;justify-content:center}
.rule{left:110px;width:978px;height:1px}
.foot-icon{width:43px;height:42px;border:2px solid var(--accent);display:flex;align-items:center;justify-content:center}
.foot-title{font-size:16px;width:300px;text-align:center}
.foot-value{font-size:15px;font-weight:500;width:300px;text-align:center}
.nav{top:3478px;font-size:14px}
.copyright{font-size:12px}
</style>
</head>
<body>

<header>
  <div class="abs hero" role="img" aria-label="City skyline at dusk behind the header"></div>
  <div class="abs city-band"></div>
  <div class="abs icon-btn" style="left:985px;top:46px">
    <svg width="20" height="16" viewBox="0 0 20 16"><path d="M4 2h14M8 8h10M4 14h14" stroke="#1a1410" stroke-width="2"/></svg>
  </div>
  <div class="abs icon-btn" style="left:1045px;top:46px">
    <svg width="18" height="16" viewBox="0 0 18 16"><path d="M1 1h3l2 9h9l2-7H5" fill="none" stroke="#1a1410" stroke-width="2"/><circle cx="7" cy="14" r="1.5" fill="#1a1410"/><circle cx="14" cy="14" r="1.5" fill="#1a1410"/></svg>
  </div>
  <div class="abs brand top">BRAMBLETON<br>MEDIA</div>
  <p class="abs tagline">SED UT PERSPICIATIS UNDE OMNIS ISTE NATUS ERROR SIT VOLUPTATEM ACCUSANTIUM DOLOREMQUE</p>
  <a class="abs btn" style="left:530px;top:366px;width:138px;height:44px">GET STARTED</a>
</header>

<section class="stream">
  <h2 class="abs" style="left:109px;top:564px">STREAM <span>VIDEO</span></h2>
  <p class="abs copy" style="left:111px;top:624px">Sed ut perspiciatis unde omnis iste natus error sit voluptatem accusantium doloremque laudantium, totam rem aperiam, eaque ipsa quae ab illo inventore veritatis et quasi architecto beatae vitae dicta sunt explicabo.</p>
  <a class="abs btn" style="left:110px;top:769px;width:115px;height:43px">READ MORE</a>
  <div class="abs photo" style="left:594px;top:538px;width:538px;height:332px;background:radial-gradient(ellipse at 60% 55%,#3a5a8a 0%,#2a3550 30%,#1a1c22 60%,var(--bg) 85%)" role="img" aria-label="Video editing desk with monitors"></div>
  <div class="abs play" style="left:1085px;top:808px"><svg width="12" height="12" viewBox="0 0 12 12"><path d="M3 1l8 5-8 5z" fill="#1a1410"/></svg></div>
</section>

<section class="talent">
  <div class="abs photo" style="left:76px;top:967px;width:518px;height:359px;background:radial-gradient(ellipse at 50% 40%,#d8c8a8 0%,#8a7a62 30%,#2a2622 60%,var(--bg) 88%)" role="img" aria-label="Studio film shoot with cameras on tripods"></div>
  <h2 class="abs" style="left:649px;top:1026px">OUR <span>MUSICAL TALENT</span></h2>
  <p class="abs copy" style="left:651px;top:1084px">Sed ut perspiciatis unde omnis iste natus error sit voluptatem accusantium doloremque laudantium, totam rem aperiam, eaque ipsa quae ab illo inventore veritatis et quasi architecto beatae vitae dicta sunt explicabo.</p>
  <a class="abs btn" style="left:652px;top:1229px;width:114px;height:43px">READ MORE</a>
</section>

<section class="merch">
  <div class="abs" style="left:0;top:1380px;width:1200px;height:560px;background:linear-gradient(180deg,var(--bg) 0%,#22201e 40%,#22201e 70%,var(--bg) 100%)" role="img" aria-label="Faint city skyline backdrop"></div>
  <h2 class="abs center" style="top:1429px">OUR <span>MERCHANDISE</span></h2>
  <div class="abs merch-card-frame"></div>
  <div class="abs" style="left:139px;top:1536px;width:250px;height:216px;background:linear-gradient(135deg,#d8d8d8,#9aa0a8 50%,#3a4a6a)" role="img" aria-label="Tablet running music software beside a keyboard"></div>
  <div class="abs" style="left:475px;top:1536px;width:250px;height:216px;background:radial-gradient(ellipse at 50% 50%,#1a1a1a 0%,#1a1a1a 30%,#ffffff 32%)" role="img" aria-label="Black printed t-shirt"></div>
  <div class="abs" style="left:812px;top:1536px;width:250px;height:216px;background:radial-gradient(ellipse at 50% 55%,#3a3a3a 0%,#6a6a6a 30%,#e8e8e8 45%)" role="img" aria-label="Dark coffee mug on a saucer"></div>
  <div class="abs merch-label" style="left:139px;top:1780px">MUSIC SOFTWARE</div>
  <div class="abs merch-label" style="left:475px;top:1780px">TSHIRT</div>
  <div class="abs merch-label" style="left:812px;top:1780px">COFFEE MUG</div>
</section>

<section class="podcast">
  <h2 class="abs" style="left:109px;top:2020px">ABOUT <span>PODCAST</span></h2>
  <p class="abs copy" style="left:111px;top:2081px">Sed ut perspiciatis unde omnis iste natus error sit voluptatem accusantium doloremque laudantium, totam rem aperiam, eaque ipsa quae ab illo inventore veritatis et quasi architecto beatae vitae dicta sunt explicabo.</p>
  <a class="abs btn" style="left:110px;top:2226px;width:115px;height:43px">READ MORE</a>
  <div class="abs photo" style="left:594px;top:1961px;width:538px;height:345px;background:radial-gradient(ellipse at 55% 55%,#2ab0d8 0%,#1a6a90 30%,#15303e 55%,var(--bg) 80%)" role="img" aria-label="Mixing console with headphones in blue light"></div>
</section>

<section class="projects">
  <h2 class="abs center" style="top:2398px">OUR <span>PROJECTS</span></h2>
  <div class="abs arrow" style="left:36px;top:2633px"><svg width="14" height="12" viewBox="0 0 14 12"><path d="M7 1L2 6l5 5M12 1L7 6l5 5" fill="none" stroke="#fff" stroke-width="1.8"/></svg></div>
  <div class="abs" style="left:116px;top:2472px;width:311px;height:367px;background:linear-gradient(160deg,#8a8a8a,#3a3a3a 55%,#1e1e1e)" role="img" aria-label="Producer at keyboards in a studio, black and white"></div>
  <div class="abs" style="left:445px;top:2472px;width:310px;height:367px;background:linear-gradient(180deg,#3a2a4a 0%,#4a3040 45%,#b8782a 70%,#2a1e28 100%)" role="img" aria-label="Lit mixing desk in warm stage light"></div>
  <div class="abs" style="left:773px;top:2472px;width:311px;height:367px;background:linear-gradient(180deg,#b8b8b8 0%,#6a6a6a 40%,#2a2a2a 100%)" role="img" aria-label="Engineer at studio monitors and rack gear, black and white"></div>
  <div class="abs arrow" style="left:1121px;top:2633px"><svg width="14" height="12" viewBox="0 0 14 12"><path d="M2 1l5 5-5 5M7 1l5 5-5 5" fill="none" stroke="#fff" stroke-width="1.8"/></svg></div>
</section>

<section class="webcast">
  <h2 class="abs center" style="top:2922px">OUR <span>WEBCAST</span></h2>
  <p class="abs center" style="top:2986px;font-size:14.5px;line-height:30px">Sed ut perspiciatis unde omnis iste natus error sit voluptatem accusantium doloremque laudantium, totam rem<br>aperiam, eaque ipsa quae ab illo inventore veritatis et quasi architecto beatae vitae dicta sunt explicabo.</p>
  <p class="abs center" style="top:3063px;font-size:14.5px;font-weight:600">Nemo enim ipsam voluptatem quia voluptas sit aspernatur aut odit aut fugit.</p>
  <a class="abs btn" style="left:543px;top:3120px;width:114px;height:41px">READ MORE</a>
</section>

<footer>
  <div class="abs rule" style="top:3207px;background:var(--accent)"></div>
  <div class="abs foot-icon" style="left:233px;top:3292px"><svg width="14" height="14" viewBox="0 0 14 14"><path d="M3 1l2.5 3-1.5 1.5c.8 1.8 2.2 3.2 4 4L9.5 8 13 10.5 11.5 13C6 13 1 8 1 2.5z" fill="#fff"/></svg></div>
  <div class="abs foot-title" style="left:104px;top:3360px">CONTACT NUMBER</div>
  <div class="abs foot-value" style="left:104px;top:3390px">+1 555 214 7730</div>
  <div class="abs brand" style="top:3318px;font-size:27px;letter-spacing:7px">BRAMBLETON<br>MEDIA</div>
  <div class="abs foot-icon" style="left:899px;top:3292px"><svg width="14" height="11" viewBox="0 0 14 11"><rect width="14" height="11" fill="#fff"/><path d="M0 0l7 6 7-6" fill="none" stroke="#141313" stroke-width="1.4"/></svg></div>
  <div class="abs foot-title" style="left:770px;top:3360px">EMAIL ADDRESS</div>
  <div class="abs foot-value" style="left:770px;top:3390px;font-weight:400;font-size:16px">INFO@BRAMBLETONMEDIA.COM</div>
  <div class="abs rule" style="top:3452px;background:#2e2b29"></div>
  <nav>
    <span class="abs nav" style="left:219px">HOME</span>
    <span class="abs nav" style="left:306px">|</span>
    <span class="abs nav" style="left:357px">ABOUT US</span>
    <span class="abs nav" style="left:469px">|</span>
    <span class="abs nav" style="left:520px">OUR MERCHANDISE</span>
    <span class="abs nav" style="left:691px">|</span>
    <span class="abs nav" style="left:743px">REVIEWS</span>
    <span class="abs nav" style="left:846px">|</span>
    <span class="abs nav" style="left:897px">CONTACT US</span>
  </nav>
  <p class="abs center copyright" style="top:3520px">(C) Copyright 2024 | All Rights Reserved</p>
</footer>

</body>
</html>
```